Design required for boutique fire engineering firm in New Zealand

Our website was published based on free Wordpress templates, we'd like something a bit more bespoke, clean and simple.
Updates

Reason: didn't check this finished on a Sunday :)

Target Market(s)

architects, building owners, property developers

Industry/Entity Type

Boutique

Contact Information for Business Card

Logo
Fire Engineering

Desmond Harlow
Principal
+64 21 482 735
desmond@veltrane.nz
veltrane.nz

Number of Pages Required

3 page

Font styles to use
Sans Serif

Requirements
Nice to have
• On the business card, an embossed logo would be great - not sure if that's a design thing or just a print thing?
• Website, existing @ http://veltrane.nz for extent of content and general arrangement that I'm happy with.
• Ability to update the content with project bio's and some photos at a later date would be nice.

```html
<!DOCTYPE html>
<html lang="en">
<head>
<meta charset="utf-8">
<title>Veltrane — Website Pages</title>
<link rel="stylesheet" href="https://fonts.googleapis.com/css2?family=Montserrat:wght@900&family=Nunito+Sans:ital,wght@0,400;0,600;0,700;0,800;1,400&display=swap">
<style>
  :root {
    --page-bg: #ffffff;
    --panel-dark: #141313;
    --ember-core: #f8880f;
    --ember: #e8710a;
    --ember-deep: rgba(165, 62, 5, 0.75);
    --ember-fade: rgba(90, 35, 5, 0.35);
    --link-orange: #f07c0c;
    --text-light: #ffffff;
    --text-soft: #ece6e0;
    --footer-band: rgba(32, 17, 4, 0.78);
    --field-fill: rgba(230, 215, 205, 0.45);
    --field-text: #2a2420;
    --label-ink: #111111;
  }
  * { box-sizing: border-box; margin: 0; padding: 0; }
  html, body { width: 1200px; height: 1200px; overflow: hidden; background: var(--page-bg); }
  body { position: relative; font-family: "Nunito Sans", sans-serif; }

  .page-label {
    position: absolute;
    font-family: "Montserrat", sans-serif;
    font-weight: 900;
    color: var(--label-ink);
    font-size: 92px;
    line-height: 1;
    letter-spacing: -1px;
    white-space: nowrap;
    transform-origin: left top;
  }
  .page-label--about { left: 1140px; top: 46px; transform: rotate(90deg); }
  .page-label--contact { left: 124px; top: 622px; transform: rotate(90deg) scaleX(0.84); }

  .site-page {
    position: absolute;
    width: 1002px;
    height: 563px;
    overflow: hidden;
    background:
      radial-gradient(ellipse 58% 52% at 50% 88%, var(--ember-core) 0%, var(--ember) 18%, var(--ember-deep) 42%, var(--ember-fade) 62%, rgba(20, 19, 19, 0) 85%),
      var(--panel-dark);
    color: var(--text-light);
  }
  .site-page--about { left: 31px; top: 21px; }
  .site-page--contact { left: 154px; top: 618px; }

  .brand { position: absolute; left: 22px; top: 18px; display: flex; align-items: center; gap: 10px; }
  .brand-dot { width: 48px; height: 48px; border: 4px solid var(--text-light); border-radius: 50%; }
  .brand-name { font-size: 40px; font-weight: 700; letter-spacing: -0.5px; line-height: 1; color: var(--text-light); }

  .main-nav { position: absolute; top: 31px; font-size: 14px; font-weight: 600; letter-spacing: 0.2px; }
  .main-nav a { position: absolute; color: var(--text-light); text-decoration: none; white-space: nowrap; }
  .main-nav a.is-active { color: var(--link-orange); font-weight: 800; }
  .main-nav .nav-about { left: 722px; }
  .main-nav .nav-contact { left: 850px; }

  .page-title {
    position: absolute; left: 0; width: 100%; text-align: center;
    font-family: "Montserrat", sans-serif; font-weight: 900;
    font-size: 60px; line-height: 1; letter-spacing: 0.5px;
  }
  .site-page--about .page-title { top: 108px; }
  .site-page--contact .page-title { top: 107px; }

  .about-copy {
    position: absolute; left: 86px; width: 830px; text-align: center;
    font-size: 13.5px; line-height: 24.6px; color: var(--text-soft);
  }
  .about-copy--intro { top: 204px; }
  .about-copy--bio { top: 302px; }

  .contact-card { position: absolute; left: 0; width: 100%; top: 178px; text-align: center; line-height: 17px; font-size: 13px; }
  .contact-card .person { font-size: 17px; font-weight: 800; line-height: 22px; }
  .contact-intro { position: absolute; left: 0; width: 100%; top: 248px; text-align: center; font-size: 13.5px; }

  .field {
    position: absolute; background: var(--field-fill);
    color: var(--field-text); font-size: 13px; font-style: italic;
    padding: 3px 7px; border: 1px solid rgba(255,255,255,0.12);
  }
  .field--name { left: 296px; top: 278px; width: 198px; height: 24px; }
  .field--email { left: 512px; top: 278px; width: 198px; height: 24px; }
  .field--subject { left: 296px; top: 317px; width: 414px; height: 24px; }
  .field--message { left: 296px; top: 352px; width: 414px; height: 74px; background: rgba(235, 195, 160, 0.55); }

  .send-button {
    position: absolute; left: 459px; top: 438px; width: 84px; height: 31px;
    background: #000; border: 2px solid var(--text-light); border-radius: 4px;
    color: var(--text-light); font-family: "Montserrat", sans-serif; font-weight: 900;
    font-size: 16px; line-height: 27px; text-align: center; letter-spacing: 0.5px;
  }

  .site-footer { position: absolute; left: 0; bottom: 0; width: 100%; height: 80px; background: var(--footer-band); }
  .copyright { position: absolute; left: 22px; top: 53px; font-size: 12px; color: var(--text-light); white-space: nowrap; }
  .copyright em { font-style: italic; }
  .copyright a { color: var(--link-orange); text-decoration: none; }
  .follow-label { position: absolute; right: 45px; top: 15px; font-size: 10.5px; color: var(--text-soft); }
  .social-links { position: absolute; left: 831px; top: 38px; display: flex; gap: 13px; }
  .social-links span { width: 26px; height: 26px; border-radius: 50%; background: var(--text-light); display: block; }
</style>
</head>
<body>

  <div class="page-label page-label--about">ABOUT US</div>

  <section class="site-page site-page--about">
    <div class="brand"><span class="brand-dot"></span><span class="brand-name">veltrane</span></div>
    <nav class="main-nav">
      <a class="nav-about is-active" href="#">ABOUT US</a>
      <a class="nav-contact" href="#">CONTACT US</a>
    </nav>
    <h1 class="page-title">ABOUT US</h1>
    <p class="about-copy about-copy--intro">Veltrane is a boutique fire engineering firm based in Wellington, New Zealand, founded by Desmond Harlow in 2017.&nbsp; We provide consulting services in the built environment, including design and review services to assist in Building Consent applications, advice on property protection matters, observation of construction on site, and regulatory consultation.</p>
    <p class="about-copy about-copy--bio">Desmond has worked as a fire engineer in New Zealand for over 20 years, having graduated from the University of Tasman Bay with a Bachelors of Engineering (with Honours) and Masters of Engineering in Fire Engineering, and is a Chartered Professional Engineer.</p>
    <footer class="site-footer">
      <p class="copyright"><em>Copyright © 2017 Veltrane.</em> Use of this website constitutes acceptance of our <a href="#">User Agreement and Privacy Policy.</a></p>
      <p class="follow-label">Follow and Like us at</p>
      <div class="social-links" aria-label="Social links"><span></span><span></span><span></span><span></span></div>
    </footer>
  </section>

  <div class="page-label page-label--contact">CONTACT US</div>

  <section class="site-page site-page--contact">
    <div class="brand"><span class="brand-dot"></span><span class="brand-name">veltrane</span></div>
    <nav class="main-nav">
      <a class="nav-about" href="#">ABOUT US</a>
      <a class="nav-contact is-active" href="#">CONTACT US</a>
    </nav>
    <h1 class="page-title">CONTACT US</h1>
    <div class="contact-card">
      <p class="person">Desmond Harlow</p>
      <p>Principal, Fire Engineer</p>
      <p>021 482 735</p>
    </div>
    <p class="contact-intro">Please send us a brief message and we will get back to you shortly.</p>
    <div class="field field--name">Name</div>
    <div class="field field--email">Email</div>
    <div class="field field--subject">Subject</div>
    <div class="field field--message">Message</div>
    <div class="send-button">SEND</div>
    <footer class="site-footer">
      <p class="copyright"><em>Copyright © 2017 Veltrane.</em> Use of this website constitutes acceptance of our <a href="#">User Agreement and Privacy Policy.</a></p>
      <p class="follow-label">Follow and Like us at</p>
      <div class="social-links" aria-label="Social links"><span></span><span></span><span></span><span></span></div>
    </footer>
  </section>

</body>
</html>
```